Business card for home decor store and design

I need a business card for my home decor boutique that’s professional looking boho/rustic. We sell vintage furniture, vintage finds, lamps, throws, rugs. We also carry a Diy paint line for refinishing furniture. We offer workshop on painting furniture, private or group setting. We in the heart of Old Town Red Bluff. We love to design, build and restore. Family owned small business. Our style is rustic boho farmhouse. We search for one of a kind found and repurposed items. We love vintage home decor, vintage windows.

Target Market(s)

Home decor

Industry/Entity Type

Home Accessories

Contact Information for Business Card

Have a rustic look/boho

Font styles to use
Serif
Script

Requirements
Must have
• Logo

```html
<!DOCTYPE html>
<html lang="en">
<head>
<meta charset="utf-8">
<title>Birch &amp; Loom Co. Business Card</title>
<link href="https://fonts.googleapis.com/css2?family=Lato:wght@400;700;900&display=swap" rel="stylesheet">
<style>
  :root {
    --backdrop: #d6d6d6;
    --card-white: #ffffff;
    --card-black: #000000;
    --ink: #0d0d0d;
    --ink-soft: #4a4a4a;
    --rule-navy: #3b3f6e;
  }
  html, body {
    margin: 0;
    padding: 0;
    width: 1200px;
    height: 1143px;
    overflow: hidden;
    background: var(--backdrop);
    font-family: "Lato", sans-serif;
  }
  .canvas {
    position: relative;
    width: 1200px;
    height: 1143px;
  }
  .card {
    position: absolute;
    left: 299px;
    width: 602px;
    height: 343px;
  }
  .card-front {
    top: 180px;
    background: var(--card-white);
    color: var(--ink);
  }
  .card-back {
    top: 621px;
    background: var(--card-black);
  }
  .brand-name {
    position: absolute;
    font-family: "Lato", sans-serif;
    font-weight: 700;
    white-space: nowrap;
    transform: translate(-50%, -50%);
  }
  .card-front .brand-name {
    left: 492px;
    top: 96px;
    font-size: 22px;
    color: var(--ink);
  }
  .card-back .brand-name {
    left: 301px;
    top: 171px;
    font-size: 34px;
    color: var(--card-white);
  }
  .holder-name {
    position: absolute;
    left: 21px;
    top: 153px;
    margin: 0;
    font-size: 29px;
    font-weight: 900;
    letter-spacing: 0.2px;
    line-height: 1;
  }
  .holder-title {
    position: absolute;
    left: 21px;
    top: 187px;
    margin: 0;
    font-size: 16px;
    color: var(--ink-soft);
    line-height: 1;
  }
  .divider {
    position: absolute;
    left: 21px;
    top: 219px;
    width: 560px;
    height: 1px;
    background: var(--rule-navy);
  }
  .contact-list {
    position: absolute;
    left: 21px;
    top: 244px;
    margin: 0;
    padding: 0;
    list-style: none;
  }
  .contact-item {
    position: absolute;
    left: 0;
    display: flex;
    align-items: center;
    white-space: nowrap;
    font-size: 16px;
    color: var(--ink-soft);
    line-height: 1;
  }
  .contact-item svg {
    width: 16px;
    height: 16px;
    margin-right: 14px;
  }
  .contact-phone { top: 0; }
  .contact-email { top: 22px; }
  .contact-web { top: 47px; }
  .address {
    position: absolute;
    right: 21px;
    top: 264px;
    margin: 0;
    text-align: right;
    font-style: normal;
    font-size: 16px;
    color: var(--ink-soft);
    line-height: 27px;
  }
</style>
</head>
<body>
<main class="canvas">
  <section class="card card-front">
    <div class="brand-name">Birch &amp; Loom Co.</div>
    <h1 class="holder-name">JOHN SMITH</h1>
    <p class="holder-title">Founder &amp; CEO</p>
    <div class="divider"></div>
    <ul class="contact-list">
      <li class="contact-item contact-phone">
        <svg viewBox="0 0 16 16" aria-hidden="true"><path d="M3.2 1.5l2.4 2.8-1.4 1.6c.9 2 2.3 3.5 4.3 4.6l1.6-1.4 2.8 2.4-1.5 2.4C6.3 13.6 2.4 9.7 1 4.2z" fill="#111"/><path d="M9.5 2.5a4.5 4.5 0 0 1 4 4M9.3 5a2 2 0 0 1 1.8 1.8" stroke="#111" stroke-width="1.2" fill="none"/></svg>
        1234567890
      </li>
      <li class="contact-item contact-email">
        <svg viewBox="0 0 16 16" aria-hidden="true"><rect x="1" y="3.5" width="14" height="10" fill="#111"/><path d="M1.5 4l6.5 5 6.5-5M1.5 13l5-4.5M14.5 13l-5-4.5" stroke="#fff" stroke-width="1" fill="none"/></svg>
        info@yourmail.com
      </li>
      <li class="contact-item contact-web">
        <svg viewBox="0 0 16 16" aria-hidden="true"><circle cx="8" cy="8" r="6.5" fill="none" stroke="#111" stroke-width="1.3"/><path d="M1.5 8h13M8 1.5v13M3 4.5h10M3 11.5h10M8 1.5c-3 3-3 10 0 13M8 1.5c3 3 3 10 0 13" stroke="#111" stroke-width="0.8" fill="none"/></svg>
        www.yourwebsite.com
      </li>
    </ul>
    <address class="address">1234 First Line Address<br>5678 Second Line Address</address>
  </section>
  <section class="card card-back">
    <div class="brand-name">Birch &amp; Loom Co.</div>
  </section>
</main>
</body>
</html>
```